Tile rush Pal page and icon

for upload to Vantrel shop page and icon 1024x500 graphic, and 512x512 icon that will represent our new word game. The game is called "Tile Rush Pal", and allows a free from arrangement of letters in a quillmark style format as they are delivered. The game will permit head to head play with others on the net, or simply a stand alone game where you can compete with yourself to get higher scores. Attached is a look at a game in progress. Obviously the "Pal" could be a creative element of this task, combined with letters. I'm completely open to ideas at this point though.

Vantrel

```html
<!DOCTYPE html>
<html lang="en">
<head>
<meta charset="utf-8">
<title>Tile Rush Pal</title>
<link rel="stylesheet" href="https://fonts.googleapis.com/css2?family=Gochi+Hand&display=swap">
<style>
  :root {
    --ink: #0a0a0a;
    --band-white: #ffffff;
    --band-edge: #8a8a8a;
    --grid-orange: #e6a15c;
    --grid-violet: #9a86c4;
    --tile-top: #ffb347;
    --tile-bottom: #ee7f12;
    --tile-edge: #b65a06;
    --tile-ink: #2a2a2a;
  }
  * { margin: 0; padding: 0; box-sizing: border-box; }
  html, body { width: 1200px; height: 2458px; overflow: hidden; background: var(--band-white); }
  .poster { position: relative; width: 1200px; height: 2458px; }

  .scene {
    position: absolute; left: 0; top: 0; width: 1200px; height: 2256px;
    background: linear-gradient(180deg,
      #8fa860 0%, #2f7fae 12%, #2a78b8 30%, #c98a6a 45%,
      #3c5f9e 62%, #2d4c98 80%, #34559f 100%);
  }

  .grid { position: absolute; left: 0; top: 0; width: 1200px; height: 2256px; }

  .board-title {
    position: absolute; left: 0; width: 1200px; text-align: center;
    font-family: "Gochi Hand", cursive; color: var(--ink);
    font-size: 330px; line-height: 1;
    z-index: 2;
  }
  .board-title--top { top: 640px; }
  .board-title--bottom { top: 1460px; }

  .tile-band {
    position: absolute; left: 0; top: 2256px; width: 1200px; height: 202px;
    background: var(--band-white);
    border-left: 22px solid var(--band-edge);
    border-top: 4px solid #cfcfcf;
    box-shadow: inset 6px 0 8px rgba(0,0,0,.25);
  }
  .tiles {
    position: absolute; top: 2276px; left: 356px;
    display: flex; gap: 14px;
  }
  .tile {
    width: 158px; height: 150px;
    background: linear-gradient(180deg, var(--tile-top), var(--tile-bottom));
    border: 3px solid var(--tile-edge);
    border-radius: 8px;
    box-shadow: 4px 6px 6px rgba(0,0,0,.35);
    display: flex; align-items: center; justify-content: center;
    font-family: "Gochi Hand", cursive;
    font-size: 110px; line-height: 1; color: var(--tile-ink);
  }
</style>
</head>
<body>
<main class="poster">
  <div class="scene" role="img" aria-label="Colour-shifted beach at sunset with a surfboard standing upright in the sand"></div>

  <svg class="grid" viewBox="0 0 1200 2256" aria-hidden="true">
    <defs>
      <pattern id="cells" width="168" height="154" patternUnits="userSpaceOnUse" x="10" y="0">
        <rect x="0" y="0" width="168" height="6" fill="var(--grid-orange)" opacity=".9"/>
        <rect x="0" y="0" width="6" height="154" fill="var(--grid-violet)" opacity=".9"/>
      </pattern>
    </defs>
    <rect width="1200" height="2256" fill="url(#cells)"/>
  </svg>

  <h1 class="board-title board-title--top">Tile</h1>
  <p class="board-title board-title--bottom">Rush</p>

  <div class="tile-band"></div>
  <div class="tiles" aria-label="Pal">
    <span class="tile">P</span>
    <span class="tile">A</span>
    <span class="tile">L</span>
  </div>
</main>
</body>
</html>
```